Veltrane Management

We need a web design for a new consulting company, with clients all over the world. The company provides management consulting to the travel industry.

Logo files are attached.

Website must look very corporate and be responsive in design.

Management Consulting

```html
<!DOCTYPE html>
<html lang="en">
<head>
<meta charset="utf-8">
<title>Veltrane Management</title>
<link rel="stylesheet" href="https://fonts.googleapis.com/css2?family=Open+Sans:wght@400;600;700&family=Oswald:wght@500&display=swap">
<style>
:root{
  --blue:#0a7ccf;
  --blue-dark:#0b5f9e;
  --text:#6f6f6f;
  --heading:#444;
  --dark:#1f2a36;
  --dark-2:#2c3947;
  --line:#e6e6e6;
  --white:#fff;
  --footer:#0d0d0d;
}
*{box-sizing:border-box;margin:0;padding:0}
html,body{width:1200px;height:2727px;overflow:hidden}
body{font-family:"Open Sans",Arial,sans-serif;color:var(--text);background:var(--white);position:relative}
h1,h2,h3{font-weight:400}
.section{position:absolute;left:0;width:1200px}
.section-title{position:absolute;left:0;width:1200px;text-align:center;font-size:23px;font-weight:400;letter-spacing:.5px}
.section-intro{position:absolute;left:280px;width:640px;text-align:center;font-size:11.5px;line-height:20px;color:#8a8a8a}

/* header */
.site-header{top:0;height:115px;background:#fafafa}
.logo{position:absolute;left:173px;top:24px;display:flex;align-items:center;gap:12px}
.logo-mark{width:62px;height:62px;border-radius:50%;background:var(--blue)}
.logo-name{font-size:38px;font-weight:700;color:var(--blue-dark);line-height:38px;letter-spacing:1px}
.logo-sub{font-size:12.5px;font-weight:700;color:var(--blue-dark);letter-spacing:1.2px}
.main-nav{position:absolute;left:593px;top:40px;display:flex;font-size:12.5px;color:#333}
.main-nav a{display:block;height:40px;line-height:40px;padding:0 17px;text-decoration:none;color:#333}
.main-nav a.active{background:var(--blue);color:var(--white)}

/* hero */
.hero{top:115px;height:540px}
.hero-photo{position:absolute;inset:0;background:linear-gradient(90deg,#e9eef1 0%,#d9dfe3 40%,#c7b8a8 70%,#9c8a7c 100%)}
.hero-title{position:absolute;left:169px;top:218px;font-family:"Oswald",Arial,sans-serif;font-weight:500;font-size:38px;line-height:56px;color:var(--blue);letter-spacing:-.5px}
.slider-arrows{position:absolute;left:171px;top:340px;display:flex;gap:7px}
.slider-arrows span{width:42px;height:42px;border-radius:50%;background:rgba(255,255,255,.55);display:flex;align-items:center;justify-content:center}
.slider-arrows span.next{background:rgba(60,60,60,.75)}

/* services */
.services{top:655px;height:518px}
.services .section-title{top:26px;color:var(--blue)}
.services .section-intro{top:62px}
.service-card{position:absolute;top:134px;width:264px;height:338px;border:1px solid var(--line);text-align:center;background:var(--white)}
.service-card.featured{background:var(--blue);border-color:var(--blue)}
.service-icon{position:absolute;left:71px;top:26px;width:122px;height:122px;border-radius:50%;background:var(--white);border:1px solid #eee;display:flex;align-items:center;justify-content:center}
.service-card.featured .service-icon{border:none}
.service-shadow{position:absolute;left:72px;top:160px;width:120px;height:14px;border-radius:50%;background:radial-gradient(#ddd,transparent 70%)}
.featured .service-shadow{background:radial-gradient(rgba(0,0,0,.18),transparent 70%)}
.service-name{position:absolute;top:189px;width:100%;font-size:12.5px;font-weight:400;color:var(--blue);text-transform:uppercase}
.featured .service-name,.featured .service-text{color:var(--white)}
.service-text{position:absolute;top:213px;left:30px;width:204px;font-size:10.5px;line-height:20px;color:var(--text)}
.btn-small{position:absolute;left:90px;top:288px;width:84px;height:30px;line-height:30px;background:var(--white);border:1px solid #eee;font-size:10.5px;color:var(--blue);text-decoration:none}

/* advantages */
.advantages{top:1173px;height:476px;background:linear-gradient(180deg,var(--dark-2),var(--dark) 60%,#17212b)}
.advantages .section-title{top:26px;color:var(--white)}
.advantage{position:absolute;width:390px;height:150px}
.adv-icon{position:absolute;left:0;top:0;width:100px;height:100px;border-radius:50%;background:var(--white);display:flex;align-items:center;justify-content:center}
.adv-name{position:absolute;left:140px;top:12px;font-size:14.5px;font-weight:400;color:var(--white);text-transform:uppercase}
.adv-text{position:absolute;left:140px;top:42px;width:236px;font-size:10.5px;line-height:20px;color:#dfe4e8;text-align:justify}
.adv-divider{position:absolute;left:172px;top:228px;width:857px;height:1px;background:rgba(255,255,255,.12)}
.btn-pill{position:absolute;left:515px;top:405px;width:178px;height:40px;line-height:40px;border-radius:20px;background:var(--blue);color:var(--white);font-size:13.5px;text-align:center;text-decoration:none}

/* news */
.news{top:1649px;height:466px}
.news .section-title{top:24px;color:var(--heading)}
.news .section-intro{top:60px}
.news-item{position:absolute;top:125px;width:271px}
.news-photo{width:271px;height:150px;background:linear-gradient(135deg,#c9d4de,#8ea3b6 60%,#4b5e72)}
.news-title{margin-top:14px;font-size:13px;color:var(--blue);font-weight:600}
.news-date{margin-top:10px;font-size:10.5px;color:#6a8a2a}
.news-text{margin-top:10px;font-size:10.5px;line-height:20px}
.news-more{display:block;margin-top:10px;font-size:10.5px;color:#555;text-decoration:none}

/* testimonials */
.testimonials{top:2115px;height:334px;background:linear-gradient(180deg,#26313d,#1b2530 55%,#2a3542)}
.testimonials .section-title{top:24px;color:var(--white)}
.quote-rule{position:absolute;left:172px;width:857px;height:1px;background:rgba(255,255,255,.2)}
.quote-text{position:absolute;left:205px;top:110px;width:790px;font-size:11.5px;line-height:22px;color:#eef;text-align:center}
.quote-mark{position:absolute;font-size:34px;font-weight:700;color:var(--blue);line-height:1}
.client-avatar{position:absolute;left:469px;top:218px;width:102px;height:102px;border-radius:50%;border:3px solid var(--white);background:linear-gradient(180deg,#d9dde2,#9aa5b1)}
.client-name{position:absolute;left:588px;top:260px;font-size:13.5px;color:var(--white)}

/* clients */
.clients{top:2449px;height:153px;background:#fbfbfb}
.client-box{position:absolute;top:20px;width:160px;height:105px;border:1px solid #eaeaea;background:var(--white);display:flex;align-items:center;justify-content:center;gap:8px}
.client-box .dot{width:16px;height:16px;border-radius:50%;background:var(--blue)}
.client-box span{font-size:21px;font-weight:700;color:#333}

/* footer */
.site-footer{top:2602px;height:125px;background:var(--footer);text-align:center}
.copyright{position:absolute;top:19px;width:100%;font-size:10.5px;color:#bbb}
.footer-nav{position:absolute;top:51px;width:100%;font-size:10.5px;color:#bbb}
.footer-nav a{color:#bbb;text-decoration:none;padding:0 6px}
.social{position:absolute;left:553px;top:80px;display:flex;gap:12px}
.social span{width:26px;height:26px;border-radius:50%;border:1px solid #666}
</style>
</head>
<body>

<header class="section site-header">
  <div class="logo">
    <div class="logo-mark"></div>
    <div>
      <div class="logo-name">VELTRANE</div>
      <div class="logo-sub">GLOBAL ADVISORY PARTNERS</div>
    </div>
  </div>
  <nav class="main-nav">
    <a class="active" href="#">HOME</a>
    <a href="#">ABOUT US</a>
    <a href="#">SERVICES</a>
    <a href="#">BLOG</a>
    <a href="#">CONTACT US</a>
  </nav>
</header>

<section class="section hero">
  <div class="hero-photo" role="img" aria-label="Business team gathered at a glass board while a consultant sketches a chart"></div>
  <h1 class="hero-title">CORPORATE MANAGEMENT<br>CONSULTING</h1>
  <div class="slider-arrows">
    <span><svg width="14" height="14" viewBox="0 0 14 14"><path d="M9 2 4 7l5 5" fill="none" stroke="#fff" stroke-width="2"/></svg></span>
    <span class="next"><svg width="14" height="14" viewBox="0 0 14 14"><path d="M5 2l5 5-5 5" fill="none" stroke="#fff" stroke-width="2"/></svg></span>
  </div>
</section>

<section class="section services">
  <h2 class="section-title">OUR SERVICES</h2>
  <p class="section-intro">Sed ut perspiciatis unde omnis iste natus error sit voluptatem accusantium doloremque laudantium, totam rem aperiam, eaque ipsa quae ab illo inventore veritatis et quasi explicabo.</p>

  <div class="service-card featured" style="left:173px">
    <div class="service-icon">
      <svg width="62" height="50" viewBox="0 0 62 50" fill="#555"><circle cx="31" cy="12" r="9"/><path d="M16 44c0-10 7-17 15-17s15 7 15 17z"/><circle cx="13" cy="17" r="7"/><path d="M0 42c0-8 5-13 12-13 2 0 3 0 5 1-3 3-4 7-4 12z"/><circle cx="49" cy="17" r="7"/><path d="M62 42c0-8-5-13-12-13-2 0-3 0-5 1 3 3 4 7 4 12z"/></svg>
    </div>
    <div class="service-shadow"></div>
    <h3 class="service-name">Corporate Management</h3>
    <p class="service-text">Lorem ipsum dolor sit amet, consectetur adipisicing elit, sed do eiusmod tempor incididunt ut labore et dolore</p>
    <a class="btn-small" href="#">Read More</a>
  </div>

  <div class="service-card" style="left:469px">
    <div class="service-icon">
      <svg width="56" height="56" viewBox="0 0 56 56" fill="none" stroke="var(--blue)" stroke-width="5"><circle cx="33" cy="20" r="10" stroke-dasharray="4 3"/><circle cx="33" cy="20" r="4" stroke-width="3"/><circle cx="16" cy="40" r="8" stroke-dasharray="3 3"/><circle cx="16" cy="40" r="3" stroke-width="2"/></svg>
    </div>
    <div class="service-shadow"></div>
    <h3 class="service-name">Management Consulting</h3>
    <p class="service-text">Lorem ipsum dolor sit amet, consectetur adipisicing elit, sed do eiusmod tempor incididunt ut labore et dolore</p>
    <a class="btn-small" href="#">Read More</a>
  </div>

  <div class="service-card" style="left:765px">
    <div class="service-icon">
      <svg width="60" height="60" viewBox="0 0 60 60" fill="none" stroke="var(--blue)" stroke-width="4"><circle cx="30" cy="30" r="26"/><path d="M30 14v17h12"/></svg>
    </div>
    <div class="service-shadow"></div>
    <h3 class="service-name">Planning</h3>
    <p class="service-text">Lorem ipsum dolor sit amet, consectetur adipisicing elit, sed do eiusmod tempor incididunt ut labore et dolore</p>
    <a class="btn-small" href="#">Read More</a>
  </div>
</section>

<section class="section advantages">
  <h2 class="section-title">OUR ADVANTAGES</h2>

  <div class="advantage" style="left:173px;top:85px">
    <div class="adv-icon"><svg width="46" height="42" viewBox="0 0 46 42" fill="none" stroke="#333" stroke-width="2.5"><rect x="3" y="3" width="32" height="24"/><path d="M13 36h12M19 27v9"/><circle cx="19" cy="15" r="5"/><rect x="36" y="22" width="7" height="14"/></svg></div>
    <h3 class="adv-name">Pro Consulting</h3>
    <p class="adv-text">Lorem ipsum dolor sit amet, consectetur adipiscing elit. Sed blandit massa vel mauris sollicitudin dignissim. Phasellus ultrices tellus eget ipsum ornare molestie</p>
  </div>

  <div class="advantage" style="left:653px;top:85px">
    <div class="adv-icon"><svg width="46" height="42" viewBox="0 0 46 42" fill="none" stroke="#333" stroke-width="2.5"><path d="M4 4v34h38"/><path d="M12 34V22M19 34V16M26 34V24"/><circle cx="32" cy="13" r="8"/></svg></div>
    <h3 class="adv-name">Innovation and Diversity</h3>
    <p class="adv-text">Lorem ipsum dolor sit amet, consectetur adipiscing elit. Sed blandit massa vel mauris sollicitudin dignissim. Phasellus ultrices tellus eget ipsum ornare molestie</p>
  </div>

  <div class="adv-divider"></div>

  <div class="advantage" style="left:173px;top:258px">
    <div class="adv-icon"><svg width="46" height="46" viewBox="0 0 46 46" fill="none" stroke="#333" stroke-width="2.5"><rect x="4" y="4" width="38" height="30"/><path d="M10 28l9-9 6 5 11-12"/><path d="M18 42h10l-5-8z" fill="#333"/></svg></div>
    <h3 class="adv-name">Professional Approach</h3>
    <p class="adv-text">Lorem ipsum dolor sit amet, consectetur adipiscing elit. Sed blandit massa vel mauris sollicitudin dignissim. Phasellus ultrices tellus eget ipsum ornare molestie</p>
  </div>

  <div class="advantage" style="left:653px;top:258px">
    <div class="adv-icon"><svg width="46" height="46" viewBox="0 0 46 46" fill="none" stroke="#333" stroke-width="2.5"><circle cx="23" cy="17" r="3" fill="#333"/><path d="M16 10a10 10 0 0 0 0 14M30 10a10 10 0 0 1 0 14M10 5a17 17 0 0 0 0 24M36 5a17 17 0 0 1 0 24"/><path d="M23 20v20M14 42h18"/></svg></div>
    <h3 class="adv-name">Sustainable Future</h3>
    <p class="adv-text">Lorem ipsum dolor sit amet, consectetur adipiscing elit. Sed blandit massa vel mauris sollicitudin dignissim. Phasellus ultrices tellus eget ipsum ornare molestie</p>
  </div>

  <a class="btn-pill" href="#">SEE HOW IT WORKS</a>
</section>

<section class="section news">
  <h2 class="section-title">LATEST NEWS</h2>
  <p class="section-intro">Sed ut perspiciatis unde omnis iste natus error sit voluptatem accusantium doloremque laudantium, totam rem aperiam, eaque ipsa quae ab illo inventore veritatis et quasi explicabo.</p>

  <article class="news-item" style="left:173px">
    <div class="news-photo" role="img" aria-label="Business team seated around a meeting table"></div>
    <h3 class="news-title">Nibh euismod tincidunt ut</h3>
    <p class="news-date">Oct 10, 2014</p>
    <p class="news-text">Lorem ipsum dolor sit amet, consectetur adipiscing elit. Sed blandit massa vel mauris sollicitudin dignissim. Phasellus ultrices tellus eget ipsum</p>
    <a class="news-more" href="#">Read More +</a>
  </article>

  <article class="news-item" style="left:466px">
    <div class="news-photo" role="img" aria-label="Two colleagues reviewing documents at a laptop"></div>
    <h3 class="news-title">Nibh euismod tincidunt ut</h3>
    <p class="news-date">Oct 10, 2014</p>
    <p class="news-text">Lorem ipsum dolor sit amet, consectetur adipiscing elit. Sed blandit massa vel mauris sollicitudin dignissim. Phasellus ultrices tellus eget ipsum</p>
    <a class="news-more" href="#">Read More +</a>
  </article>

  <article class="news-item" style="left:759px">
    <div class="news-photo" role="img" aria-label="Businesswoman standing in front of her team in an office"></div>
    <h3 class="news-title">Nibh euismod tincidunt ut</h3>
    <p class="news-date">Oct 10, 2014</p>
    <p class="news-text">Lorem ipsum dolor sit amet, consectetur adipiscing elit. Sed blandit massa vel mauris sollicitudin dignissim. Phasellus ultrices tellus eget ipsum</p>
    <a class="news-more" href="#">Read More +</a>
  </article>
</section>

<section class="section testimonials" role="img" aria-label="Blurred city skyline behind client testimonial">
  <h2 class="section-title">WHAT OUR CLIENTS SAY</h2>
  <div class="quote-rule" style="top:85px"></div>
  <span class="quote-mark" style="left:182px;top:108px">&ldquo;</span>
  <p class="quote-text">Lorem ipsum dolor sit amet, consectetur adipiscing elit, sed do eiusmod tempor incididunt ut labore et dolore magna aliqua. Ut enim ad minim veniam, quis nostrud exercitation ullamco laboris nisi ut aliquip ex ea commodo consequat. Duis aute irure dolor in reprehenderit in voluptate velit esse cillum dolore eu fugiat nulla pariatur. Excepteur sint occaecat cupidatat non proident, sunt in culpa qui officia deserunt</p>
  <span class="quote-mark" style="left:998px;top:150px">&rdquo;</span>
  <div class="quote-rule" style="top:196px"></div>
  <div class="client-avatar" role="img" aria-label="Portrait of client Martin Hale"></div>
  <p class="client-name">Martin Hale</p>
</section>

<section class="section clients">
  <div class="client-box" style="left:173px"><span>Plenvar</span></div>
  <div class="client-box" style="left:349px"><span>Driskelo</span></div>
  <div class="client-box" style="left:522px"><span>Omantrix</span></div>
  <div class="client-box" style="left:696px"><span>Vezurin</span></div>
  <div class="client-box" style="left:871px"><i class="dot"></i><span>Teluvra</span></div>
</section>

<footer class="section site-footer">
  <p class="copyright">&copy;2014 VELTRANE , ALL RIGHTS RESERVED.</p>
  <nav class="footer-nav">
    <a href="#">HOME</a>| <a href="#">ABOUT</a>| <a href="#">SERVICES</a>| <a href="#">BLOG</a>| <a href="#">CONTACT</a>
  </nav>
  <div class="social"><span></span><span></span><span></span></div>
</footer>

</body>
</html>
```